Whey Protein Packet Label Design

Company background:

Company name: Fernwick Vale

Website: fernwickvale-example.com

Summary: We offer single serving supplements on the go that are all natural. We are all about healthy living and portable packaging that makes it easy to drink anywhere. Our Whey Protein Packet saves time and is convenient for our customers to make a protein shake anywhere, there is no prep time, cook time, or clean up time. These protein packets can be added into any shaker and it is easily mixed, no more large bulk tubs of protein needed anymore because we offer single servings that are manageable to carry around.

Style: Our company name is Fernwick Vale, so in our logo we are saying that anyone can reach the mountain peak by taking healthy foods. That somehow needs to be shown through a pattern or something.

Products: Whey Protein Packets, Energy Sticks, Recovery Sticks

Product Label Instruction:

I need a product label for the Whey Protein Packet for 5 flavors.
-There should be one generic design, and the flavors just change according to color scheme and pictures

1. Strawberry Banana Smoothie (100% Organic Fruit Powder)
color scheme: Red, white, brown
2. Peanut Butter Smoothie (100% Organic Nut Powder)
color scheme: light brown, brown, white
3. Chocolate Smoothie(100% Organic Cacao Powder)
color scheme: dark brown, brown, white
4. Vanilla Shake (100% Pure Vanilla Powder)
color scheme: light cream, brown, white
5. Banana Peanut Butter Shake (100% Organic Fruit & Nut Powder)
color scheme: yellow, brown, white

Each flavor label design should have this text/information on the front:

1. Logo (attached) - does not need to be main part of design( just placed somewhere is fine)
2. Natural Whey Protein Packet (product title)
3. Flavor Name
4. Flavor Picture
5. 30G (amount of protein in each packet)
6. 4 professional stamps that easily state (attached an image for example)
1. Non GMO
2. Gluten Free
3. Lactose Free
4. No Artificial Flavoring
7. Net Weight 36G

Colors: I would like to use flavor color, brown, and white mainly for the packaging but I am open to different colors for diff flavors and colorful pictures.

Ideas: Please give me multiple designs to look at for the first draft.

Other company examples: I have attached some pictures of other packaging designs that I like that you can keep in mind.

Target Market(s)

Upscale, organic lifestyle, vegans, on the go people, police force, outdoor people, health junkies, gym goers, men and women

I hope you can make something that will appeal to most or all of these categories.

Industry/Entity Type

It Company

Requirements
Must have
• label dimensions: 3 x 3.75
• font: Unique, not something basic that looks like it came off of word document. It needs to look professional and unique that the upscale market would like.
Nice to have
• I have attached some examples of other companies that I like the look of. That is the type of style I am going for.
Should not have
• It should not be a basic design that I can make myself. I am looking for a professional who can make the product look like an organic style and shows that we offer HIGH QUALITY, high end supplements.

```html
<!DOCTYPE html>
<html lang="en">
<head>
<meta charset="utf-8">
<title>Fernwick Vale – Natural Whey Protein Packet Label</title>
<link rel="stylesheet" href="https://fonts.googleapis.com/css2?family=Antonio:wght@200;300&family=Quicksand:wght@500;600&display=swap">
<style>
  :root {
    --backdrop: #d9d9d9;
    --label-white: #ffffff;
    --flavor-red: #d71920;
    --rock-red-light: #e8232b;
    --rock-red-dark: #9a0f15;
    --title-brown: #3b1a13;
    --stamp-grey: #8b8b8b;
    --stamp-ring: #ffffff;
  }
  * { margin: 0; padding: 0; box-sizing: border-box; }
  html, body {
    width: 1200px; height: 794px; overflow: hidden;
    background: var(--backdrop);
  }
  .label {
    position: absolute; left: 320px; top: 47px;
    width: 560px; height: 700px;
    background: var(--label-white);
    overflow: hidden;
    font-family: "Quicksand", sans-serif;
  }
  .hero-scene {
    position: absolute; left: 0; top: 0;
    width: 560px; height: 700px;
  }
  .brand-name {
    position: absolute; left: 300px; width: 240px; top: 48px;
    text-align: center;
    font-family: "Quicksand", sans-serif; font-weight: 500;
    font-size: 30px; letter-spacing: 2px;
    color: var(--flavor-red);
    text-transform: uppercase;
  }
  .product-title {
    position: absolute; right: 59px; top: 148px;
    text-align: right;
    font-family: "Antonio", sans-serif; font-weight: 300;
    font-size: 62px; line-height: 58px;
    color: var(--title-brown);
    text-transform: uppercase;
  }
  .flavor-band {
    position: absolute; left: 182px; right: 0; top: 397px; height: 151px;
    background: var(--flavor-red);
    color: var(--label-white);
    text-align: right;
    padding-right: 59px;
  }
  .flavor-name {
    margin-top: 25px;
    font-weight: 600; font-size: 26px; line-height: 30px;
    text-transform: uppercase;
  }
  .flavor-source {
    margin-top: 8px; margin-left: 64px;
    border-top: 1.5px solid var(--label-white);
    padding-top: 7px;
    font-weight: 500; font-size: 18px; line-height: 20px;
  }
  .net-weight {
    margin-top: 6px; margin-left: 137px;
    border-top: 1.5px solid var(--label-white);
    padding-top: 6px;
    font-weight: 500; font-size: 16px; line-height: 18px;
  }
  .stamps {
    position: absolute; left: 155px; top: 559px;
    display: flex; gap: 8px;
  }
  .stamp {
    width: 80px; height: 80px; border-radius: 50%;
    background: var(--stamp-grey);
    display: flex; align-items: center; justify-content: center;
    position: relative;
  }
  .stamp::after {
    content: ""; position: absolute; inset: 5px;
    border: 1.5px solid var(--stamp-ring); border-radius: 50%;
  }
  .stamp-text {
    color: var(--label-white);
    font-weight: 600; font-size: 10px; line-height: 11px;
    text-align: center; text-transform: uppercase;
    transform: rotate(-14deg);
    width: 62px;
  }
</style>
</head>
<body>
  <main class="label">
    <svg class="hero-scene" viewBox="0 0 560 700" role="img" aria-label="Red-toned photo of a rock cliff with a climber silhouette hanging on a rope">
      <defs>
        <linearGradient id="rockTone" x1="0" y1="0" x2="1" y2="1">
          <stop offset="0" stop-color="var(--rock-red-light)"/>
          <stop offset="1" stop-color="var(--rock-red-dark)"/>
        </linearGradient>
      </defs>
      <path d="M0 0 H222 L212 110 L238 250 L222 330 L175 420 L150 540 L128 700 H0 Z" fill="url(#rockTone)"/>
    </svg>

    <div class="brand-name">Fernwick Vale</div>

    <h1 class="product-title">Natural Whey<br>Protein Packet</h1>

    <section class="flavor-band">
      <h2 class="flavor-name">Strawberry<br>Banana Smoothie</h2>
      <p class="flavor-source">(100% Organic Fruit Powder)</p>
      <p class="net-weight">NET WT.: 30G</p>
    </section>

    <ul class="stamps">
      <li class="stamp"><span class="stamp-text">Non GMO</span></li>
      <li class="stamp"><span class="stamp-text">Gluten Free</span></li>
      <li class="stamp"><span class="stamp-text">Lactose Free</span></li>
      <li class="stamp"><span class="stamp-text">No Artificial Flavoring</span></li>
    </ul>
  </main>
</body>
</html>
```